Tess Marlowe Communication business card

I am starting a small, country-based business that offers writing, communication and marketing services to a wide range of clients, inner city big business, to mining, through to agriculture.

The appeal of my business is that it's mobile and flexible. It's just me, with lots of hands-on experience on construction and infrastructure projects.

I can provide the following services:

• Communication planning and management
• Issues and media management
• Marketing and communication materials
• Project management and strategy
• Government liaison
• Incident management communication
• Stakeholder management

It would be great to be able to use the elements of the business card design on other stationery.

Industry/Entity Type

Communication

Requirements
Must have
• The following information:

Tess Marlowe
M: 0427 391 864
E: tess@tmcommsmail.com

PO Box 152
Durrandale Q 4472
Nice to have
• a rural element (windmill, workboots, wheat stalk)

```html
<!DOCTYPE html>
<html lang="en">
<head>
<meta charset="utf-8">
<title>Tess Marlowe Communication – Business Card</title>
<link href="https://fonts.googleapis.com/css2?family=Questrial&family=Arimo:wght@400&display=swap" rel="stylesheet">
<style>
  :root {
    --teal: #1fa3a3;
    --teal-dark: #137e7e;
    --band-text: #e9f7f6;
    --ink: #555a5c;
    --ink-soft: #6b7072;
    --rule: #8d9193;
    --card: #f4f4f2;
    --backdrop: #d9dadb;
  }
  * { box-sizing: border-box; margin: 0; padding: 0; }
  html, body {
    width: 1200px; height: 900px; overflow: hidden;
    background: var(--backdrop);
  }
  .card {
    position: absolute; left: 100px; top: 164px;
    width: 1000px; height: 572px;
    background: var(--card);
    box-shadow: 0 10px 30px rgba(0,0,0,0.18);
    overflow: hidden;
  }
  .identity {
    position: absolute; left: 48px; top: 236px;
    width: 370px; text-align: right;
  }
  .identity__name {
    font-family: "Questrial", sans-serif;
    font-size: 66px; line-height: 1; color: var(--teal);
    letter-spacing: -1px; white-space: nowrap;
  }
  .identity__role {
    font-family: "Questrial", sans-serif;
    font-size: 30px; color: var(--ink); margin-top: 4px;
  }
  .divider {
    position: absolute; left: 444px; top: 56px;
    width: 1px; height: 346px; background: var(--rule);
  }
  .services {
    position: absolute; left: 474px; top: 70px;
    list-style: none;
    font-family: "Arimo", sans-serif; font-size: 22px;
    color: var(--ink-soft); line-height: 40px;
  }
  .services li::before { content: "• "; }
  .contact-band {
    position: absolute; left: 0; bottom: 0;
    width: 100%; height: 136px; background: var(--teal);
    font-family: "Arimo", sans-serif; color: var(--band-text);
  }
  .contact-band__address {
    position: absolute; left: 474px; top: 20px; font-size: 22px;
  }
  .contact-item {
    position: absolute; top: 72px;
    display: flex; align-items: center; gap: 12px; font-size: 22px;
  }
  .contact-item--phone { left: 214px; }
  .contact-item--email { left: 600px; }
  .contact-item svg { width: 30px; height: 30px; flex: none; }
</style>
</head>
<body>
  <main class="card">
    <div class="identity">
      <h1 class="identity__name">Tess Marlowe</h1>
      <p class="identity__role">Ceo Manager</p>
    </div>
    <div class="divider"></div>
    <ul class="services">
      <li>Communication planning and management</li>
      <li>Problems and media management</li>
      <li>Marketing materials</li>
      <li>Project management and strategy</li>
      <li>Government Liaison</li>
      <li>Incident management communication</li>
      <li>Stakeholder management</li>
    </ul>
    <footer class="contact-band">
      <p class="contact-band__address">PO Box 152 Durrandale Q 4472</p>
      <p class="contact-item contact-item--phone">
        <svg viewBox="0 0 30 30" aria-hidden="true">
          <circle cx="15" cy="15" r="14" fill="#e9f7f6"/>
          <path d="M10.5 8.5l3 3-1.6 1.9c.9 1.8 2.3 3.2 4.1 4.1l1.9-1.6 3 3-1.8 2.1c-5.2-.5-10.1-5.4-10.6-10.6z" fill="#137e7e"/>
        </svg>
        0427 391 864
      </p>
      <p class="contact-item contact-item--email">
        <svg viewBox="0 0 30 30" aria-hidden="true">
          <circle cx="15" cy="15" r="14" fill="#e9f7f6"/>
          <rect x="8" y="10" width="14" height="10" rx="1" fill="#137e7e"/>
          <path d="M8.5 10.8l6.5 5 6.5-5" fill="none" stroke="#e9f7f6" stroke-width="1.4"/>
        </svg>
        tess@tmcommsmail.com
      </p>
    </footer>
  </main>
</body>
</html>
```